Striking new Advert required for Commercial Real Estate Agency

We need a a NEW newspaper advertisement for the marketing of a large commercial property (a Backpackers lodge)

Dimensions are to be width of 101mm and height of 100mm (10cms)

Our key design statement for this advert is clean, modern and minimalist design, with accents of 'HOT PINK' colour to remove it from looking too boring, perhaps in the area of the contact icons. The heirachy of the advert is outlined in the attached ADVERTISEMENT TEXT FILE.

Our company name is THE VANTREL COLLECTIVE, and we want our brand to appear professional yet classy in it's design style (sort of like an advertising or design agency)

We have two logo options below, one more square in its layout (which we prefer) and the other more rectangular, which may be better suited for the layout. We are not adverse to the logo being reversed (white text on black), along with other key element areas such as the main advert heading and the "FOR SALE" part, and think this would be a good option.
There are two photos attached to be included in the advert.

We have attached an example of an old advert that we did, which we DID NOT LIKE, and which was for a smaller width than the one we need (it is only 65% of the width of this one). WE have also atached a file showing layout of some of our competitors adverts, which we dont think are too good either.

We are really open for ideas, but have time pressures, so please come back with any questions as soon as you can, if needed.

Thank you
Updates

Thank you for the great and diverse designs. There are a few standout options, but one style that we prefer most.

Target Market(s)

We are wanting this newspaper advertisement to attract interest from real estat e developers, investors and motel/lodge owners, along with other high nett worth individuals

Industry/Entity Type

Real Estate

Font styles to use
Serif
Sans Serif

Colors
1b1b1b
a54499
474747
fbfbfb

Requirements
Must have
• Clean modern look, predominantly monochromatic or black and white, with the hot pink accent somewhere, as mentioned above.
• All the contents of the TEXT provided, perhaps with additional space to add a little more if needed, Please advise if you think we dont have enough space for all of the TEXT
Should not have
• Script like fonts
• Cartoonish characters
• a 'cheap' look

```html
<!DOCTYPE html>
<html lang="en">
<head>
<meta charset="utf-8">
<title>Mount Victoria Land Grab – For Sale</title>
<link rel="stylesheet" href="https://fonts.googleapis.com/css2?family=Arimo:wght@700&family=Open+Sans:wght@400;600;700&display=swap">
<style>
  :root {
    --ink: #000000;
    --charcoal: #1b1b1b;
    --slate: #474747;
    --paper: #fbfbfb;
    --white: #ffffff;
    --hot-pink: #a54499;
  }
  html, body {
    margin: 0;
    width: 1200px;
    height: 1200px;
    overflow: hidden;
    background: var(--paper);
  }
  .advert {
    display: block;
    width: 1200px;
    height: 1200px;
  }
  .headline { font-family: "Arimo", Arial, sans-serif; font-weight: 700; fill: var(--white); }
  .copy { font-family: "Open Sans", Arial, sans-serif; }
  .copy-dark { fill: var(--ink); }
  .copy-light { fill: var(--white); }
  .agent-name { fill: var(--hot-pink); font-weight: 700; }
  .strong { font-weight: 700; }
  .brand-name { font-family: "Open Sans", Arial, sans-serif; font-weight: 600; fill: var(--ink); }
  .icon-pink { fill: var(--hot-pink); }
  .icon-stroke { fill: none; stroke: var(--hot-pink); stroke-width: 2; }
</style>
</head>
<body>
<svg class="advert" viewBox="0 0 1193 1181" preserveAspectRatio="none" xmlns="http://www.w3.org/2000/svg">
  <defs>
    <linearGradient id="building-photo" x1="0" y1="0" x2="0" y2="1">
      <stop offset="0" stop-color="#7fa3d6"/>
      <stop offset="0.35" stop-color="#c9d3e0"/>
      <stop offset="1" stop-color="#8a8f99"/>
    </linearGradient>
    <linearGradient id="aerial-photo" x1="0" y1="0" x2="1" y2="1">
      <stop offset="0" stop-color="#9aa58a"/>
      <stop offset="0.5" stop-color="#8c8f86"/>
      <stop offset="1" stop-color="#7f9a3e"/>
    </linearGradient>
    <radialGradient id="badge-fill" cx="0.5" cy="0.5" r="0.5">
      <stop offset="0.6" stop-color="#ffffff"/>
      <stop offset="1" stop-color="#bdbdbd"/>
    </radialGradient>
  </defs>

  <rect width="1193" height="1181" fill="var(--white)"/>

  <g class="header">
    <polygon points="0,0 565,0 677,237 84,237" fill="var(--slate)"/>
    <polygon points="0,0 14,0 92,237 84,237" fill="var(--white)"/>
    <polygon points="0,42 81,237 0,237" fill="var(--ink)"/>
    <polygon points="20,24 552,24 636,196 87,196" fill="var(--ink)"/>
    <text class="headline" x="316" y="100" font-size="58" text-anchor="middle">FOR SALE</text>
    <text class="headline" x="342" y="158" font-size="40" text-anchor="middle">Mount Victoria Land Grab</text>
  </g>

  <g class="contact copy">
    <text class="copy-dark" x="968" y="54" font-size="28" text-anchor="middle">Contact the <tspan class="strong">Sole Agenct</tspan></text>
    <text class="agent-name" x="968" y="104" font-size="36" text-anchor="middle">Marcus Delaney</text>
    <path class="icon-pink" d="M716,130 c-4,2 -6,6 -5,12 c2,12 8,22 16,28 c4,2 8,1 10,-2 l2,-3 l-7,-6 l-3,3 c-5,-3 -9,-10 -10,-16 l3,-2 l-4,-9 z"/>
    <text class="copy-dark" x="745" y="154" font-size="29">(04) 555 0192</text>
    <rect class="icon-pink" x="949" y="126" width="14" height="30" rx="2"/>
    <rect x="952" y="131" width="8" height="7" fill="var(--white)"/>
    <rect class="icon-pink" x="950" y="118" width="2" height="9"/>
    <text class="copy-dark" x="968" y="154" font-size="29">(021) 555 0148</text>
    <rect class="icon-pink" x="714" y="186" width="24" height="16"/>
    <path d="M714,186 l12,9 l12,-9" fill="none" stroke="var(--white)" stroke-width="2"/>
    <text class="copy-dark" x="745" y="204" font-size="29">marcus@vantrelcollective.co.nz</text>
  </g>

  <polygon points="95,248 614,248 704,620 225,620" fill="url(#building-photo)" role="img" aria-label="Photo looking up at the weatherboard lodge building with balconies"/>
  <polygon points="622,248 1193,248 1193,620 712,620" fill="url(#aerial-photo)" role="img" aria-label="Aerial photo of the lodge, car park and surrounding suburb"/>

  <rect x="693" y="556" width="500" height="66" fill="var(--slate)"/>
  <text class="copy copy-light" x="1167" y="600" font-size="32" text-anchor="end">Now Selling by <tspan class="strong">Closed Tender</tspan></text>

  <polygon points="226,624 1193,624 1193,690 250,690" fill="var(--ink)"/>
  <text class="copy copy-light" x="708" y="662" font-size="32" text-anchor="middle">Corlett’s Lodge, 42 Harwood Street, Mount Victoria</text>

  <g class="brand-badge">
    <circle cx="155" cy="469" r="136" fill="url(#badge-fill)" stroke="var(--ink)" stroke-width="12"/>
    <text class="brand-name" x="155" y="462" font-size="24" text-anchor="middle">The Vantrel</text>
    <text class="brand-name" x="155" y="494" font-size="24" text-anchor="middle">Collective</text>
  </g>

  <g class="details copy">
    <rect x="0" y="702" width="1193" height="406" fill="var(--ink)"/>
    <rect x="0" y="737" width="48" height="13" fill="var(--white)"/>
    <rect x="1097" y="737" width="96" height="13" fill="var(--white)"/>
    <text class="copy-light" x="572" y="753" font-size="33" text-anchor="middle">This Old Beauty has served many, and is now ripe for development.</text>

    <text class="copy-light" font-size="27">
      <tspan x="48" y="803">One of Mt Vic’s largest land areas, now offered with vacant possession, with key</tspan>
      <tspan x="48" y="843">details being:</tspan>
      <tspan x="48" y="893">Large Land area of 2076m² with elevated sunny position and great outlook + access</tspan>
      <tspan x="48" y="933">from Alder Street</tspan>
      <tspan x="48" y="983">Existing Backpackers Lodge of 970m² providing multiple rooms with amenity areas</tspan>
      <tspan x="48" y="1033" word-spacing="10">Four adjacent sites also available, taking total land area to 4452m², an</tspan>
      <tspan x="48" y="1075" word-spacing="6">unprecedented Land Offering in this popular cuity fringe location</tspan>
    </text>

    <g fill="none" stroke="var(--white)" stroke-width="4" stroke-linecap="round" stroke-linejoin="round">
      <path d="M23,883 l6,7 l12,-16"/>
      <path d="M23,973 l6,7 l12,-16"/>
      <path d="M23,1023 l6,7 l12,-16"/>
    </g>
  </g>

  <g class="footer copy">
    <circle class="icon-stroke" cx="316" cy="1140" r="13"/>
    <ellipse class="icon-stroke" cx="316" cy="1140" rx="6" ry="13"/>
    <path class="icon-stroke" d="M303,1140 h26 M305,1133 h22 M305,1147 h22"/>
    <text class="copy-dark" x="351" y="1149" font-size="31" letter-spacing="2.5">www.vantrelcollective.co.nz</text>
  </g>
</svg>
</body>
</html>
```